KORBALT

The business want a professional looking business card. We have a scetch we will add but want the extra upgrade, and would like more suggestions for variations of our business cards.

```html
<!DOCTYPE html>
<html lang="en">
<head>
<meta charset="UTF-8">
<title>KORBALT – Business Card</title>
<link href="https://fonts.googleapis.com/css2?family=Cinzel:wght@500;600&family=Montserrat:wght@400;500&display=swap" rel="stylesheet">
<style>
  :root {
    --page: #e9e2d6;
    --forest: #123b2e;
    --gold: #c9a05a;
    --gold-soft: #d8bf91;
    --cream: #f4f0e7;
    --ink: #173a2f;
    --body-ink: #2f3a35;
    --mark-faint: #e2d5bd;
  }
  * { box-sizing: border-box; margin: 0; padding: 0; }
  html, body {
    width: 1200px; height: 1000px; overflow: hidden;
    background: var(--page);
  }
  .canvas { position: relative; width: 1200px; height: 1000px; }

  .card {
    position: absolute;
    border-radius: 34px;
    box-shadow: 0 10px 30px rgba(60, 45, 25, 0.18);
  }

  /* Front */
  .card-front {
    left: 140px; top: 110px; width: 660px; height: 400px;
    background: var(--forest);
    color: var(--gold);
    display: flex; flex-direction: column; align-items: center;
    padding-top: 70px;
  }
  .front-dot {
    width: 22px; height: 22px; border-radius: 50%;
    background: var(--gold); margin-bottom: 34px;
  }
  .front-name {
    font-family: "Cinzel", serif; font-weight: 600;
    font-size: 62px; letter-spacing: 0.08em; line-height: 1;
  }
  .front-sub {
    display: flex; align-items: center; gap: 22px;
    font-family: "Cinzel", serif; font-weight: 600;
    font-size: 24px; letter-spacing: 0.42em;
    margin-top: 16px;
  }
  .front-sub .rule { width: 60px; height: 2px; background: var(--gold); }
  .front-since {
    display: flex; align-items: center; gap: 14px;
    font-family: "Montserrat", sans-serif; font-weight: 500;
    font-size: 13px; letter-spacing: 0.32em;
    margin-top: 18px;
  }
  .front-since .rule { width: 70px; height: 1.5px; background: var(--gold); }

  /* Back */
  .card-back {
    left: 410px; top: 470px; width: 700px; height: 420px;
    background: var(--cream);
    display: flex;
  }
  .back-info { width: 400px; padding: 68px 0 0 58px; }
  .back-name {
    font-family: "Cinzel", serif; font-weight: 600;
    font-size: 34px; letter-spacing: 0.06em; color: var(--ink); line-height: 1;
  }
  .back-sub {
    font-family: "Cinzel", serif; font-weight: 600;
    font-size: 16px; letter-spacing: 0.5em; color: var(--ink);
    margin-top: 10px;
  }
  .back-role {
    font-family: "Montserrat", sans-serif; font-size: 16px;
    color: var(--body-ink); line-height: 1.45; margin-top: 20px;
  }
  .back-rule {
    width: 258px; height: 1.5px; background: var(--gold);
    margin: 14px 0 24px;
  }
  .contact-list { list-style: none; }
  .contact-list li {
    display: flex; align-items: center; gap: 18px;
    font-family: "Montserrat", sans-serif; font-size: 15px;
    color: var(--body-ink); margin-bottom: 14px;
  }
  .contact-list svg { width: 18px; height: 18px; flex: none; }

  .back-divider {
    width: 1.5px; height: 230px; background: var(--gold);
    margin-top: 104px;
  }
  .back-mark-area {
    flex: 1; display: flex; flex-direction: column; align-items: center;
    padding-top: 100px;
  }
  .back-circle {
    width: 140px; height: 140px; border-radius: 50%;
    background: var(--mark-faint);
  }
  .back-since {
    font-family: "Montserrat", sans-serif; font-weight: 500;
    font-size: 13px; letter-spacing: 0.32em; color: var(--gold);
    margin-top: 40px;
  }
</style>
</head>
<body>
<main class="canvas">

  <section class="card card-front" aria-label="Business card front">
    <div class="front-dot"></div>
    <h1 class="front-name">KORBALT</h1>
    <div class="front-sub"><span>BREKKELI</span><span class="rule"></span></div>
    <div class="front-since"><span class="rule"></span><span>SINCE 2024</span><span class="rule"></span></div>
  </section>

  <section class="card card-back" aria-label="Business card back">
    <div class="back-info">
      <h2 class="back-name">KORBALT</h2>
      <p class="back-sub">BREKKELI</p>
      <p class="back-role">CEO &amp; Founder<br>Lars Erik Brekkeli</p>
      <div class="back-rule"></div>
      <ul class="contact-list">
        <li>
          <svg viewBox="0 0 24 24" fill="var(--ink)"><path d="M6.6 10.8a15 15 0 0 0 6.6 6.6l2.2-2.2c.3-.3.7-.4 1-.2 1.1.4 2.3.6 3.6.6.6 0 1 .4 1 1V20c0 .6-.4 1-1 1A17 17 0 0 1 3 4c0-.6.4-1 1-1h3.5c.6 0 1 .4 1 1 0 1.3.2 2.5.6 3.6.1.3 0 .7-.2 1z"/></svg>
          004791234567
        </li>
        <li>
          <svg viewBox="0 0 24 24" fill="none" stroke="var(--ink)" stroke-width="2"><rect x="3" y="5" width="18" height="14" rx="1.5" fill="var(--ink)"/><path d="M3.5 6l8.5 7 8.5-7" stroke="var(--cream)"/></svg>
          korbalt.llc@postmail.no
        </li>
        <li>
          <svg viewBox="0 0 24 24" fill="none" stroke="var(--ink)" stroke-width="1.8"><circle cx="12" cy="12" r="9"/><ellipse cx="12" cy="12" rx="4" ry="9"/><path d="M3 12h18M5 7.5h14M5 16.5h14"/></svg>
          www.korbalt.llc
        </li>
      </ul>
    </div>
    <div class="back-divider"></div>
    <div class="back-mark-area">
      <div class="back-circle"></div>
      <p class="back-since">SINCE 2024</p>
    </div>
  </section>

</main>
</body>
</html>
```